Marks of Dunmore business card design

I need a clean, professional looking design using the attached logo with a bright green/ gray/dark gray/black colors. Maybe even an orange accent if it looks good. I am open to slight changes in the logo if needed. Details below on the info on what should be on the cards. We are a sign company in Ft. Lauderdale FL that specializes in yacht lettering on multi million dollar yachts.

Target Market(s)

marine industry, yachts

Industry/Entity Type

Business

Colors
9bcb3c
000000
606060
f37122

Requirements
Must have
• address: 2847 W. Harlow Rd.
• Pompano Beach, FL 33417
• Phone: 954-518-3046
• email/website: marksofdunmore@mailvista.net MarksofDunmore.net
Nice to have
• I would like it very clean and simple but professional looking. Nice layout and would prefer a darker background. Orange highlight only if it works.
Should not have
• Nothing fancy.

```html
<!DOCTYPE html>
<html lang="en">
<head>
<meta charset="utf-8">
<title>Marks of Dunmore – Business Card</title>
<link rel="stylesheet" href="https://fonts.googleapis.com/css2?family=Open+Sans:wght@400;700;800&display=swap">
<style>
  :root {
    --stage: #3a3431;
    --card: #0e0e0e;
    --green: #1fa84f;
    --orange: #f37122;
    --grey-light: #c9c9c9;
    --white: #f2f2f2;
  }
  * { margin: 0; padding: 0; box-sizing: border-box; }
  html, body { width: 1200px; height: 900px; overflow: hidden; }
  body {
    background: var(--stage);
    font-family: "Open Sans", Arial, sans-serif;
    display: flex;
    align-items: center;
    justify-content: center;
    gap: 40px;
  }
  .card {
    position: relative;
    width: 540px;
    height: 310px;
    background: var(--card);
    box-shadow: 0 10px 30px rgba(0,0,0,.45);
  }
  .card-front .wordmark {
    position: absolute;
    top: 58px;
    left: 0;
    right: 0;
    text-align: center;
    font-weight: 800;
    font-size: 38px;
    letter-spacing: -0.5px;
    color: var(--green);
  }
  .card-front .name-row {
    position: absolute;
    top: 150px;
    left: 34px;
    right: 34px;
    display: flex;
    align-items: center;
    gap: 14px;
  }
  .card-front .person-name {
    font-weight: 800;
    font-size: 20px;
    text-transform: uppercase;
    color: var(--green);
    white-space: nowrap;
  }
  .card-front .rule {
    flex: 1;
    height: 1px;
    background: var(--green);
  }
  .card-front .person-role {
    position: absolute;
    top: 178px;
    left: 34px;
    font-size: 14px;
    color: var(--orange);
  }
  .card-front .address {
    position: absolute;
    top: 180px;
    right: 34px;
    text-align: right;
    font-size: 13px;
    line-height: 1.45;
    color: var(--white);
  }
  .card-front .contacts {
    position: absolute;
    top: 214px;
    left: 34px;
    list-style: none;
    font-size: 14px;
    line-height: 1.45;
    color: var(--white);
  }
  .card-front .contacts li { display: flex; align-items: center; gap: 8px; }
  .card-front .contacts svg { width: 11px; height: 11px; fill: var(--green); flex: none; }
  .card-back {
    display: flex;
    align-items: center;
    justify-content: center;
  }
  .card-back .wordmark {
    font-weight: 800;
    font-size: 40px;
    letter-spacing: -0.5px;
    color: var(--grey-light);
  }
</style>
</head>
<body>
  <section class="card card-front">
    <div class="wordmark">Marks of Dunmore</div>
    <div class="name-row">
      <span class="person-name">Daniel Dunmore</span>
      <span class="rule"></span>
    </div>
    <div class="person-role">Owner</div>
    <address class="address">2847 W. Harlow Rd.<br>Pompano Beach, FL 33417</address>
    <ul class="contacts">
      <li>
        <svg viewBox="0 0 24 24" aria-hidden="true"><path d="M6.6 10.8a15.1 15.1 0 0 0 6.6 6.6l2.2-2.2a1 1 0 0 1 1-.25 11.4 11.4 0 0 0 3.6.57 1 1 0 0 1 1 1V20a1 1 0 0 1-1 1A17 17 0 0 1 3 4a1 1 0 0 1 1-1h3.5a1 1 0 0 1 1 1c0 1.25.2 2.45.57 3.57a1 1 0 0 1-.25 1z"/></svg>
        954-518-3046
      </li>
      <li>
        <svg viewBox="0 0 24 24" aria-hidden="true"><path d="M2 5h20v14H2z M2 5l10 8 10-8" fill-rule="evenodd"/><path d="M2 5l10 8 10-8" fill="none" stroke="#0e0e0e" stroke-width="2"/></svg>
        marksofdunmore@mailvista.net
      </li>
      <li>
        <svg viewBox="0 0 24 24" aria-hidden="true"><circle cx="12" cy="12" r="11"/><path d="M1 12h22M12 1c4 4 4 18 0 22M12 1c-4 4-4 18 0 22" fill="none" stroke="#0e0e0e" stroke-width="1.6"/></svg>
        www.MarksofDunmore.net
      </li>
    </ul>
  </section>

  <section class="card card-back">
    <div class="wordmark">Marks of Dunmore</div>
  </section>
</body>
</html>
```